New Business Card Design Project

I need a design for business cards, i am an electrical business called "Vantor Electrical and Communications" i need the cards to be double sided with the company logo on the back (attached) the front needs to say my company name, web site, email address, telephone number, and ABN number and electrical license number. I am open to different arrangements of the information but would like the background to be incorporating something electrical or something that looks smart. open to all additional ideas also.

The company colours are orange and grey see logo attached.

Business Name: Vantor Electrical and Communications
Website: vantorelectricalandcomms.example.au
Email: dean@vantorelectricalandcomms.example.au
Telephone(mobile): 0481290736
ABN: 71829304516
Lic No: 483027D

Target Market(s)

Business entities, Project Managers, Accounts, Clients

Industry/Entity Type

Electrician

Contact Information for Business Card

I need a design for business cards, i am an electrical business called "Vantor Electrical and Communications" i need the cards to be double sided with the company logo on the back (attached) the front needs to say my company name

Font styles to use
Serif
Sans Serif

Colors
f37122
5c5c5c

Requirements
Must have
• Must have the Logo on the back open to different ways of it being on the back but had in mind to keep it central but again open to other options
Nice to have
• A real modern cool background that is eye catching yet contemporary
Should not have
• No backgrounds of a light bulb or plug or anything like that

```html
<!DOCTYPE html>
<html lang="en">
<head>
<meta charset="utf-8">
<title>Vantor Electrical and Communications – Business Card</title>
<link href="https://fonts.googleapis.com/css2?family=Open+Sans:wght@400;600&display=swap" rel="stylesheet">
<style>
  :root{
    --bg:#232323;
    --grey:#5c5c5c;
    --grey-dark:#4e4e4e;
    --orange:#f37122;
    --amber:#ffa10f;
    --amber-light:#ffc23a;
    --white:#ffffff;
  }
  *{margin:0;padding:0;box-sizing:border-box}
  html,body{width:1200px;height:1200px;overflow:hidden;background:var(--bg)}
  body{font-family:"Open Sans",sans-serif;position:relative}
  .card{position:absolute;left:120px;width:960px;height:531px;overflow:hidden}
  .card-front{top:46px;background:var(--orange)}
  .card-back{top:623px;background:var(--grey)}

  /* front */
  .front-header{position:absolute;left:0;top:0;width:100%;height:132px;background:var(--grey)}
  .header-name{position:absolute;left:28px;top:48px;font-size:26px;font-weight:600;color:var(--white);letter-spacing:1px}
  .header-divider{position:absolute;left:178px;top:34px;width:2px;height:66px;background:#8a8a8a}
  .header-title{position:absolute;left:222px;top:46px;font-size:31px;color:var(--orange)}
  .header-circuit{position:absolute;right:0;top:0;width:200px;height:132px;
    background:linear-gradient(135deg,rgba(255,255,255,0) 20%,rgba(255,255,255,.22) 60%,rgba(255,255,255,.08));}
  .contacts{position:absolute;left:197px;top:182px;list-style:none}
  .contacts li{display:flex;align-items:center;height:56px;font-size:26px;color:var(--white)}
  .contacts svg{width:38px;height:38px;margin-right:26px;flex:none}
  .footer-art{position:absolute;left:0;top:0}
  .footer-circuit{position:absolute;left:140px;top:400px;width:640px;height:131px;
    background:linear-gradient(90deg,rgba(255,210,60,.0),rgba(255,214,70,.55) 35%,rgba(255,214,70,.3) 70%,rgba(255,214,70,0));
    clip-path:polygon(9% 0,100% 0,100% 100%,0 100%)}
  .reg{position:absolute;left:735px;display:flex;align-items:center;font-size:19px;color:var(--grey-dark)}
  .reg-abn{top:415px}
  .reg-lic{top:462px}
  .reg-badge{width:36px;height:36px;border-radius:50%;background:var(--grey);color:var(--white);
    font-size:11px;font-weight:600;display:flex;align-items:center;justify-content:center;margin-right:20px;line-height:1;text-align:center}

  /* back */
  .side-strip{position:absolute;top:0;width:180px;height:100%;background:var(--orange)}
  .side-strip.left{left:0}
  .side-strip.right{right:0}
  .strip-circuit{position:absolute;left:0;top:160px;width:100%;height:190px;
    background:linear-gradient(180deg,rgba(255,200,60,0),rgba(255,200,60,.55) 30%,rgba(255,200,60,.55) 70%,rgba(255,200,60,0))}
  .brand{position:absolute;left:180px;right:180px;top:0;bottom:0;display:flex;align-items:center;justify-content:center;gap:22px}
  .brand-dot{width:34px;height:34px;border-radius:50%;background:var(--orange)}
  .brand-name{font-size:118px;font-weight:400;color:var(--white);letter-spacing:8px}
</style>
</head>
<body>

<section class="card card-front" aria-label="Business card front">
  <div class="front-header">
    <div class="header-name">VANTOR</div>
    <div class="header-divider"></div>
    <div class="header-title">Vantor Electrical and Communications</div>
    <div class="header-circuit" role="img" aria-label="Circuit board trace pattern"></div>
  </div>

  <ul class="contacts">
    <li>
      <svg viewBox="0 0 38 38"><circle cx="19" cy="19" r="19" fill="#5c5c5c"/><rect x="13" y="9" width="12" height="20" rx="2" fill="none" stroke="#fff" stroke-width="2"/><rect x="15.5" y="12" width="7" height="5" fill="#fff"/><g fill="#fff"><rect x="15.5" y="19" width="2" height="2"/><rect x="20.5" y="19" width="2" height="2"/><rect x="15.5" y="23" width="2" height="2"/><rect x="20.5" y="23" width="2" height="2"/></g></svg>
      0481290736
    </li>
    <li>
      <svg viewBox="0 0 38 38"><circle cx="19" cy="19" r="19" fill="#5c5c5c"/><rect x="10" y="12" width="18" height="14" rx="1.5" fill="#fff"/><path d="M10 13l9 7 9-7" fill="none" stroke="#5c5c5c" stroke-width="2"/></svg>
      dean@vantorelectricalandcomms.example.au
    </li>
    <li>
      <svg viewBox="0 0 38 38"><circle cx="19" cy="19" r="19" fill="#5c5c5c"/><g fill="none" stroke="#fff" stroke-width="1.6"><circle cx="19" cy="19" r="10"/><ellipse cx="19" cy="19" rx="4.5" ry="10"/><path d="M9 19h20M10.5 14h17M10.5 24h17M19 9v20"/></g></svg>
      www.vantorelectricalandcomms.example.au
    </li>
  </ul>

  <svg class="footer-art" width="960" height="531" viewBox="0 0 960 531">
    <path d="M305 362 Q318 350 340 350 H960 V531 H305 Z" fill="#5c5c5c"/>
    <path d="M280 381 Q260 381 248 395 L140 531 H960 V381 Z" fill="#ffa10f"/>
    <path d="M0 440 H100 Q120 440 110 460 L75 531 H0 Z" fill="#ffa10f"/>
  </svg>
  <div class="footer-circuit" role="img" aria-label="Circuit board trace pattern"></div>

  <div class="reg reg-abn"><span class="reg-badge">ABN</span>71829304516</div>
  <div class="reg reg-lic"><span class="reg-badge">Lic<br>No</span>&nbsp;&nbsp;483027D</div>
</section>

<section class="card card-back" aria-label="Business card back">
  <div class="side-strip left"><div class="strip-circuit" role="img" aria-label="Circuit board trace pattern"></div></div>
  <div class="side-strip right"><div class="strip-circuit" role="img" aria-label="Circuit board trace pattern"></div></div>
  <div class="brand">
    <span class="brand-dot"></span>
    <span class="brand-name">VANTOR</span>
  </div>
</section>

</body>
</html>
```